Dental Office Business Card

We need a business card for our pediatric dentistry office.
On one side the design needs to contain the following:
our logo (attached)
Vento Pediatric Grins
Soraya Kadbelani, DDS
Board Certified Pediatric Dentist
Tel: (555) 318-2747)
Fax: (555) 264-8031
Email: info@ventopediatricgrins.example
Web: www.ventopediatricgrins.example
Address: 41 Brindle Ave, Suite 208, Fernhollow, VT 02099

On the other side of the card, the design needs to have an appointment reminder (date and time as well as day of the week) similar to the design attached (no need for appointment reason “For”)

```html
<!DOCTYPE html>
<html lang="en">
<head>
<meta charset="utf-8">
<title>Vento Pediatric Grins – Business Card</title>
<link href="https://fonts.googleapis.com/css2?family=Poppins:ital,wght@0,300;0,400;0,600;0,700;1,300;1,400&display=swap" rel="stylesheet">
<style>
  :root {
    --mint: #a6d5a8;
    --ink: #231f20;
    --black: #070808;
    --paper: #ffffff;
    --mist: #f2f7f3;
    --backdrop: #e1e2e4;
  }
  * { margin: 0; padding: 0; box-sizing: border-box; }
  html, body { width: 960px; height: 1200px; overflow: hidden; }
  body {
    background: var(--backdrop);
    font-family: "Poppins", sans-serif;
    color: var(--ink);
    position: relative;
  }
  .card { position: absolute; left: 60px; width: 840px; height: 480px; overflow: hidden; }
  .card--front { top: 94px; background: var(--paper); }
  .card--back { top: 626px; background: var(--mist); }

  .card__blobs { position: absolute; inset: 0; }

  /* Brand block */
  .brand { position: absolute; left: 78px; top: 172px; display: flex; align-items: center; gap: 12px; }
  .brand__dot { width: 44px; height: 44px; border-radius: 50%; background: var(--mint); flex: none; }
  .brand__name { font-weight: 700; font-size: 28px; line-height: 1.1; color: var(--ink); width: 230px; }
  .brand__rule { position: absolute; left: 93px; top: 267px; width: 274px; height: 2px; background: var(--ink); }
  .doctor { position: absolute; left: 93px; top: 276px; }
  .doctor__name { font-weight: 700; font-size: 22px; color: var(--mint); line-height: 1.3; white-space: nowrap; }
  .doctor__title { font-size: 11px; color: var(--ink); line-height: 1.4; }

  /* Contact column */
  .contact-bar { position: absolute; left: 402px; top: 0; width: 37px; height: 363px; background: var(--ink); border-radius: 0 0 19px 19px; }
  .contact__icon { position: absolute; left: 408px; width: 26px; height: 26px; }
  .contact__text { position: absolute; left: 453px; font-size: 18px; line-height: 24px; color: var(--ink); white-space: nowrap; }

  /* Appointment side */
  .reminder__band { position: absolute; left: 0; top: 62px; width: 100%; height: 45px; background: var(--black); }
  .reminder__title { position: absolute; left: 0; top: 58px; width: 100%; text-align: center; font-weight: 300; font-size: 45px; letter-spacing: 12px; text-indent: 12px; color: var(--mint); line-height: 52px; }
  .reminder__subtitle { position: absolute; left: 0; top: 117px; width: 100%; text-align: center; font-style: italic; font-weight: 300; font-size: 30px; letter-spacing: 7px; text-indent: 7px; color: var(--black); line-height: 36px; }
  .field__label { position: absolute; left: 90px; font-weight: 300; font-size: 30px; line-height: 36px; color: var(--black); }
  .field__line { position: absolute; left: 201px; height: 2px; background: var(--black); }
  .days { position: absolute; top: 278px; left: 0; width: 100%; height: 34px; }
  .day { position: absolute; top: 0; display: flex; align-items: flex-end; font-style: italic; font-weight: 300; font-size: 26px; line-height: 30px; color: var(--black); }
  .day__box { width: 27px; height: 27px; border: 1.5px solid var(--black); margin-right: 3px; margin-bottom: 1px; }
  .meridiem { position: absolute; left: 413px; top: 372px; font-style: italic; font-weight: 300; font-size: 25px; color: var(--black); word-spacing: 8px; }
</style>
</head>
<body>

<section class="card card--front" aria-label="Business card front">
  <svg class="card__blobs" viewBox="0 0 840 480" width="840" height="480" aria-hidden="true">
    <path fill="var(--mint)" d="M0 0 H321 C318 40 280 46 240 58 C180 76 150 120 110 150 C75 175 40 172 0 172 Z"/>
    <path fill="var(--mint)" d="M0 224 C40 232 62 280 58 330 C54 380 28 420 41 480 H0 Z"/>
    <path fill="var(--mint)" d="M840 200 C800 212 784 240 782 290 C780 360 770 400 720 420 C660 440 610 445 590 480 H840 Z"/>
  </svg>

  <div class="brand">
    <span class="brand__dot"></span>
    <span class="brand__name">Vento Pediatric Grins</span>
  </div>
  <div class="brand__rule"></div>
  <div class="doctor">
    <p class="doctor__name">Soraya Kadbelani, DDS</p>
    <p class="doctor__title">Board Certified Pediatric Dentist</p>
  </div>

  <div class="contact-bar"></div>

  <svg class="contact__icon" style="top:117px" viewBox="0 0 26 26" aria-hidden="true">
    <circle cx="13" cy="13" r="13" fill="var(--mint)"/>
    <path d="M13 6 a5 5 0 0 1 5 5 c0 4 -5 9 -5 9 s-5 -5 -5 -9 a5 5 0 0 1 5 -5z" fill="none" stroke="var(--ink)" stroke-width="1.6"/>
    <circle cx="13" cy="11" r="1.8" fill="var(--ink)"/>
  </svg>
  <p class="contact__text" style="top:118px">41 Brindle Ave,<br>Suite 208, Fernhollow,<br>VT 02099</p>

  <svg class="contact__icon" style="top:222px" viewBox="0 0 26 26" aria-hidden="true">
    <circle cx="13" cy="13" r="13" fill="var(--mint)"/>
    <path d="M8 7 l3 -1 l2 4 l-2 1.5 c1 2 2 3 4 4 l1.5 -2 l4 2 l-1 3 c-6 1 -12 -5 -11.5 -11.5z" fill="var(--ink)"/>
  </svg>
  <p class="contact__text" style="top:223px">(555) 318-2747)</p>

  <svg class="contact__icon" style="top:259px" viewBox="0 0 26 26" aria-hidden="true">
    <circle cx="13" cy="13" r="13" fill="var(--mint)"/>
    <rect x="6.5" y="8.5" width="13" height="9" fill="none" stroke="var(--ink)" stroke-width="1.5"/>
    <path d="M6.5 8.5 l6.5 5 l6.5 -5 M6.5 17.5 l4.5 -4 M19.5 17.5 l-4.5 -4" fill="none" stroke="var(--ink)" stroke-width="1.3"/>
  </svg>
  <p class="contact__text" style="top:260px">info@ventopediatricgrins.example</p>

  <svg class="contact__icon" style="top:296px" viewBox="0 0 26 26" aria-hidden="true">
    <circle cx="13" cy="13" r="13" fill="var(--mint)"/>
    <rect x="9" y="5.5" width="8" height="5" fill="none" stroke="var(--ink)" stroke-width="1.4"/>
    <rect x="7" y="10" width="12" height="10" rx="1" fill="var(--ink)"/>
    <rect x="9.5" y="13" width="7" height="1.3" fill="var(--mint)"/>
    <rect x="9.5" y="16" width="7" height="1.3" fill="var(--mint)"/>
  </svg>
  <p class="contact__text" style="top:297px">(555) 264-8031</p>

  <svg class="contact__icon" style="top:329px" viewBox="0 0 26 26" aria-hidden="true">
    <circle cx="13" cy="13" r="13" fill="var(--mint)"/>
    <g fill="none" stroke="var(--ink)" stroke-width="1.3">
      <circle cx="13" cy="13" r="7"/>
      <ellipse cx="13" cy="13" rx="3" ry="7"/>
      <path d="M6 13 H20 M7.2 9.5 H18.8 M7.2 16.5 H18.8"/>
    </g>
  </svg>
  <p class="contact__text" style="top:331px">www.ventopediatricgrins.example</p>
</section>

<section class="card card--back" aria-label="Appointment reminder">
  <div class="reminder__band"></div>
  <h1 class="reminder__title">APPOINTMENT</h1>
  <h2 class="reminder__subtitle">REMINDER</h2>

  <p class="field__label" style="top:180px">date :</p>
  <div class="field__line" style="top:209px; width:493px"></div>

  <div class="days">
    <span class="day" style="left:90px"><span class="day__box"></span>mon</span>
    <span class="day" style="left:202px"><span class="day__box"></span>tue</span>
    <span class="day" style="left:294px"><span class="day__box"></span>wed</span>
    <span class="day" style="left:399px"><span class="day__box"></span>thurs</span>
    <span class="day" style="left:516px"><span class="day__box"></span>fri</span>
    <span class="day" style="left:586px"><span class="day__box"></span>sat</span>
    <span class="day" style="left:675px"><span class="day__box"></span>sun</span>
  </div>

  <p class="field__label" style="top:364px">time :</p>
  <div class="field__line" style="top:392px; width:189px"></div>
  <p class="meridiem">a.m. p.m.</p>
</section>

</body>
</html>
```